Varneck Law Business cards and stationary design project

We are looking for a stationary design for business cards (double sided), 8x10, 5x7, and legal and standard envelopes.

We would like the design to match the logo that we have already.
Color palate preferred is Teal, White, grey and any others that will look good for a professional law firm.

We would like this statement: "RELATIONSHIPS. RESPECT. RESULT" to be on the back of the business cards and maybe on the stationary if it looks good.

Please see link to website for more information: www.varneck-law-example.com

Target Market(s)

Potential clients that need Attorney services.

Industry/Entity Type

Law Firm

Contact Information for Business Card

We would like the front and back to be two different colors. Current business cards are teal front, grey back and are a vertical design. We are open to options with colors.

Font styles to use
Serif

Colors
33a6d7
33b8a4
b9b9b9
5c5c5c

Requirements
Must have
• Logo supplied needs to go on the card and stationary.
• Match website color palate, www.varneck-law-example.com
• Be professional and not too wordy.
• Criminal Law, Civil Litigation, Personal Injury, Restraining Orders need to be on the card.
Nice to have
• RELATIONSHIPS. RESPECT. RESULTS. on the back of the card.
Should not have
• Not be too busy/wordy or too flashy.

```html
<!DOCTYPE html>
<html lang="en">
<head>
<meta charset="UTF-8">
<title>Varneck Law Stationery</title>
<link href="https://fonts.googleapis.com/css2?family=Libre+Baskerville:wght@400;700&display=swap" rel="stylesheet">
<style>
  :root {
    --teal: #1c9aa5;
    --teal-dark: #16848e;
    --charcoal: #353637;
    --charcoal-deep: #252627;
    --gold: #b59a5a;
    --paper: #ffffff;
    --backdrop: #d8d9da;
    --rule-grey: #e3e5e6;
  }
  * { box-sizing: border-box; margin: 0; padding: 0; }
  html, body { width: 876px; height: 1200px; overflow: hidden; }
  body {
    background: var(--backdrop);
    font-family: "Libre Baskerville", "Times New Roman", serif;
    position: relative;
  }
  .piece { position: absolute; box-shadow: 0 3px 10px rgba(0,0,0,0.22); }

  /* Business card — back */
  .card-back {
    left: 15px; top: 73px; width: 315px; height: 190px;
    background: linear-gradient(160deg, var(--charcoal) 0%, var(--charcoal-deep) 100%);
    color: #e9e9e9;
    text-align: center;
  }
  .card-back .wordmark {
    position: absolute; left: 0; right: 0; top: 62px;
    font-size: 22px; letter-spacing: 1px; color: #f2f2f2;
  }
  .card-back .gold-rule {
    position: absolute; left: 18px; right: 18px; top: 150px;
    height: 2px; background: var(--gold);
  }
  .card-back .tagline {
    position: absolute; left: 0; right: 0; top: 158px;
    font-size: 10.5px; letter-spacing: 0.6px; color: #ededed;
  }

  /* Business card — front */
  .card-front {
    left: 345px; top: 73px; width: 516px; height: 190px;
    background: var(--teal); color: var(--paper);
  }
  .card-front .wordmark {
    position: absolute; left: 30px; top: 28px;
    font-size: 20px; letter-spacing: 0.5px;
  }
  .card-front .services {
    position: absolute; left: 30px; top: 74px;
    list-style: none; font-weight: 700; font-size: 14px; line-height: 21px;
  }
  .card-front .name-plate {
    position: absolute; left: 330px; top: 14px; width: 170px; height: 36px;
    background: var(--paper); color: var(--teal-dark); padding: 4px 10px;
  }
  .name-plate .name { font-weight: 700; font-size: 13px; }
  .name-plate .title { font-size: 7.5px; margin-top: 2px; }
  .card-front .contact {
    position: absolute; left: 330px; top: 70px;
    list-style: none; font-size: 8.5px; line-height: 15px;
  }
  .contact li { display: flex; align-items: flex-start; gap: 5px; }
  .contact svg { flex: none; margin-top: 3px; }

  /* Envelope front */
  .envelope-front {
    left: 111px; top: 307px; width: 750px; height: 423px;
    background: var(--paper);
  }
  .envelope-front .side-band {
    position: absolute; left: 0; top: 0; bottom: 0; width: 22px; background: var(--teal);
  }
  .envelope-front .wordmark {
    position: absolute; left: 60px; top: 80px;
    font-size: 30px; color: var(--teal); letter-spacing: 1px;
  }
  .envelope-front .stamp { position: absolute; left: 565px; top: 30px; }
  .envelope-front .rule {
    position: absolute; left: 22px; right: 0; height: 3px; background: var(--teal);
  }
  .envelope-front .rule.upper { top: 290px; }
  .envelope-front .rule.lower { top: 362px; }
  .envelope-front .tagline {
    position: absolute; left: 22px; right: 0; top: 314px; text-align: center;
    font-weight: 700; font-size: 21px; letter-spacing: 2px; color: var(--teal);
  }

  /* Envelope back */
  .envelope-back {
    left: 111px; top: 765px; width: 750px; height: 388px;
    background: var(--paper);
  }
  .envelope-back .flap {
    position: absolute; left: 0; right: 0; top: 0; height: 111px; background: var(--teal);
  }
  .envelope-back .flap-shade {
    position: absolute; left: 0; right: 0; top: 111px; height: 8px;
    background: linear-gradient(var(--rule-grey), var(--paper));
  }
  .envelope-back .wordmark {
    position: absolute; left: 0; right: 0; top: 48px; text-align: center;
    font-size: 22px; color: var(--paper); letter-spacing: 1px;
  }
</style>
</head>
<body>

  <section class="piece card-back" aria-label="Business card back">
    <div class="wordmark">Varneck Law</div>
    <div class="gold-rule"></div>
    <p class="tagline">RELATIONSHIPS | RESPECT | RESULTS</p>
  </section>

  <section class="piece card-front" aria-label="Business card front">
    <div class="wordmark">Varneck Law</div>
    <ul class="services">
      <li>Criminal Law</li>
      <li>Civil Litigation</li>
      <li>Personal Injury</li>
      <li>Restraining Orders</li>
    </ul>
    <div class="name-plate">
      <div class="name">Dana Merrow</div>
      <div class="title">Experienced Trial Attorney</div>
    </div>
    <ul class="contact">
      <li><svg width="8" height="8" viewBox="0 0 8 8"><rect width="8" height="8" rx="1.5" fill="#fff"/></svg>ph (555) 010-2947</li>
      <li><svg width="8" height="8" viewBox="0 0 8 8"><rect width="8" height="8" rx="1.5" fill="#fff"/></svg>dana@varneck-law-example.com</li>
      <li><svg width="8" height="8" viewBox="0 0 8 8"><rect width="8" height="8" rx="1.5" fill="#fff"/></svg>www.varneck-law-example.com</li>
      <li><svg width="8" height="10" viewBox="0 0 8 10"><path d="M4 0a4 4 0 0 1 4 4c0 3-4 6-4 6S0 7 0 4a4 4 0 0 1 4-4z" fill="#fff"/><circle cx="4" cy="4" r="1.5" fill="#1c9aa5"/></svg><span>120 Harbor Ave, Suite 200<br>Bayview City, CA 90000</span></li>
    </ul>
  </section>

  <section class="piece envelope-front" aria-label="Envelope front">
    <div class="side-band"></div>
    <div class="wordmark">Varneck Law</div>
    <svg class="stamp" width="105" height="125" viewBox="0 0 105 125" aria-label="Stamp placement">
      <rect x="3" y="3" width="99" height="119" fill="none" stroke="#9a9a9a" stroke-width="4" stroke-dasharray="5 3"/>
      <rect x="10" y="10" width="85" height="105" fill="#fafafa" stroke="#bdbdbd" stroke-width="1"/>
    </svg>
    <div class="rule upper"></div>
    <p class="tagline">RELATIONSHIPS | RESPECT | RESULTS</p>
    <div class="rule lower"></div>
  </section>

  <section class="piece envelope-back" aria-label="Envelope back">
    <div class="flap"></div>
    <div class="flap-shade"></div>
    <div class="wordmark">Varneck Law</div>
  </section>

</body>
</html>
```